Roost 'n run. Chicken shop

yDesign special menu with special pictures within 48 h
Very smaple menu

Target Market(s)

Local

Industry/Entity Type

Food

Colors
FFF300
FFF600
FEFA6F
FFFEC7
FFFEE8

Requirements
Must have
• IGood quality picture
Nice to have
• Good quality pictures

```html
<!DOCTYPE html>
<html lang="en">
<head>
<meta charset="utf-8">
<title>Roost 'n run — Menu</title>
<link rel="stylesheet" href="https://fonts.googleapis.com/css2?family=Poppins:wght@500;600;700;800&family=Questrial&display=swap">
<style>
:root{
  --bg-top:#FDB630;
  --bg-bottom:#FBA82B;
  --panel:#E54E25;
  --accent:#EC5A22;
  --tab:#F47B24;
  --ink:#3A2415;
  --ink-soft:#5A3A20;
  --cream:#FFF4D9;
  --dot-yellow:#FFC233;
  --dash-dark:#5B2A17;
  --dash-light:#FFC54A;
  --menu-word:#F6A23A;
}
*{margin:0;padding:0;box-sizing:border-box}
html,body{width:1200px;height:848px;overflow:hidden}
body{background:linear-gradient(180deg,var(--bg-top),var(--bg-bottom));font-family:"Questrial",sans-serif;color:var(--ink);position:relative}
.abs{position:absolute}
.photo{position:absolute}
.photo-left{left:0;top:0;width:270px;height:165px;border-radius:0 0 140px 0;background:radial-gradient(ellipse at 35% 40%,#E0621F 0%,#E98A2E 45%,rgba(251,176,48,0) 75%)}
.photo-right{right:0;top:0;width:300px;height:190px;border-radius:0 0 0 160px;background:radial-gradient(ellipse at 60% 45%,#D8621E 0%,#E8862E 45%,rgba(251,176,48,0) 78%)}
.brand{left:0;width:1200px;top:22px;text-align:center}
.brand-name{font-family:"Poppins",sans-serif;font-weight:800;font-size:50px;letter-spacing:1px;color:var(--accent);line-height:1;text-transform:uppercase}
.brand-sub{font-family:"Poppins",sans-serif;font-weight:500;font-size:34px;letter-spacing:4px;color:var(--menu-word);margin-top:12px;line-height:1}

.panel{left:25px;top:148px;width:476px;height:421px;background:var(--panel);border-radius:9px;color:#fff}
.panel-head{position:absolute;top:30px;text-align:center}
.panel-head h2{font-family:"Poppins",sans-serif;font-weight:700;font-size:15px;line-height:1.2;white-space:nowrap;letter-spacing:-0.2px}
.panel-head p{font-size:9.5px;margin-top:3px;white-space:nowrap}
.head-wings{left:20px;width:180px}
.head-wings h2{font-size:16px}
.head-tenders{left:212px;width:255px}
.head-tenders h2{color:var(--ink)}
.head-tenders p{color:#FFD9C0}
.step-box{position:absolute;left:17px;width:443px;border:1.3px dashed var(--dash-dark);border-radius:6px}
.step-box.light{border-color:var(--dash-light)}
.step-tab{position:absolute;left:50%;top:-10px;transform:translateX(-50%);background:var(--tab);color:#fff;font-family:"Poppins",sans-serif;font-weight:600;font-size:9px;padding:2px 9px;border-radius:3px}
.opt{position:absolute;font-size:10px;display:flex;align-items:center;gap:7px;white-space:nowrap}
.dot{width:8px;height:8px;border-radius:50%;background:#fff;flex:none}
.dot.dark{background:#3B3B3B}
.dot.yellow{background:var(--dot-yellow)}
.leader{display:inline-block;width:45px;border-bottom:1px dashed #FFB08C;margin:0 8px;transform:translateY(-2px)}
.price-s{font-family:"Poppins",sans-serif;font-weight:600;font-size:9px}

.sec-title{font-family:"Poppins",sans-serif;font-weight:500;font-size:15.5px;color:var(--accent)}
.sec-note{font-size:9.5px;color:var(--ink);margin-top:6px}
.item{position:absolute;left:534px;width:280px}
.item h3{font-family:"Poppins",sans-serif;font-weight:600;font-size:11px;color:var(--ink)}
.item p{font-size:9.3px;color:var(--ink-soft);line-height:1.3;margin-top:2px;width:215px}
.item .price{position:absolute;right:0;top:0;font-family:"Poppins",sans-serif;font-weight:600;font-size:12.5px;color:var(--accent)}
.build{position:absolute;left:857px;width:296px}
.build h4{font-size:9.5px;color:var(--ink)}
.build h4 b{font-family:"Poppins",sans-serif;font-weight:600;font-size:11px}
.build .price{position:absolute;right:0;top:0;font-family:"Poppins",sans-serif;font-weight:600;font-size:12.5px;color:var(--accent)}
.choices{display:grid;margin-top:7px;row-gap:6px;font-size:9.5px;color:var(--ink-soft)}
.choices span{display:flex;align-items:center;gap:8px;white-space:nowrap}
.choices .dot{background:var(--cream)}

.sides{left:26px;top:618px;width:1152px;height:190px;border:1.3px dashed var(--accent);border-radius:10px}
.sides-tab{position:absolute;left:474px;top:-14px;width:257px;height:30px;border-radius:15px;background:var(--accent);color:#fff;font-family:"Poppins",sans-serif;font-weight:500;font-size:15px;text-align:center;line-height:30px}
.divider{position:absolute;top:28px;height:150px;border-left:1px solid #F58A30}
.side{position:absolute;width:260px}
.side h3{font-family:"Poppins",sans-serif;font-weight:600;font-size:11px;color:var(--ink)}
.side p{font-size:9.3px;color:var(--ink-soft);line-height:1.3;margin-top:3px;width:200px}
.side .price{position:absolute;right:0;top:0;font-family:"Poppins",sans-serif;font-weight:600;font-size:12.5px;color:var(--accent)}
.extras{position:absolute;left:321px;top:123px;display:grid;row-gap:8px;font-size:9.5px;color:var(--ink-soft)}
.extras span{display:flex;align-items:center;gap:8px}
.extras .dot{background:var(--cream)}
</style>
</head>
<body>

<div class="photo photo-left" role="img" aria-label="Photo of a chicken burger with fries and fried wings"></div>
<div class="photo photo-right" role="img" aria-label="Photo of glazed chicken wings"></div>

<header class="abs brand">
  <div class="brand-name">Roost 'n run</div>
  <div class="brand-sub">MENU</div>
</header>

<section class="abs panel">
  <div class="panel-head head-wings"><h2>Breaded Wings</h2><p>All Wings Servied With Fries &amp; 1 Dip</p></div>
  <div class="panel-head head-tenders"><h2>Buttermilk Marinated Tenders</h2><p>ALL Tenders SERVIED WITH FRIES &amp; 1 Dip</p></div>

  <div class="step-box" style="top:91px;height:36px">
    <span class="step-tab">Step 1</span>
    <span class="opt" style="left:12px;top:12px"><i class="dot"></i>Wings</span>
    <span class="opt" style="left:92px;top:12px"><i class="dot"></i>Boneless</span>
    <span class="opt" style="left:272px;top:12px"><i class="dot dark"></i>Large</span>
    <span class="opt" style="left:350px;top:12px"><i class="dot dark"></i>Mini</span>
  </div>

  <div class="step-box" style="top:143px;height:92px">
    <span class="step-tab">Step 2</span>
    <span class="opt" style="left:10px;top:10px"><i class="dot"></i><span style="width:55px;text-align:right">4 wings</span><i class="leader"></i><span class="price-s">6.99 £</span></span>
    <span class="opt" style="left:10px;top:30px"><i class="dot"></i><span style="width:55px;text-align:right">8 wings</span><i class="leader"></i><span class="price-s">9.75£</span></span>
    <span class="opt" style="left:10px;top:50px"><i class="dot"></i><span style="width:55px;text-align:right">10 wings</span><i class="leader"></i><span class="price-s">11.50£</span></span>
    <span class="opt" style="left:10px;top:72px"><i class="dot"></i><span style="width:55px;text-align:right">12 wings</span><i class="leader"></i><span class="price-s">12.95£</span></span>
    <span class="opt" style="left:270px;top:9px"><i class="dot dark"></i><span style="width:58px;text-align:right">3 Tenders</span><i class="leader"></i><span class="price-s">5.99£</span></span>
    <span class="opt" style="left:270px;top:29px"><i class="dot dark"></i><span style="width:58px;text-align:right">6 Tenders</span><i class="leader"></i><span class="price-s">8.99 £</span></span>
  </div>

  <div class="step-box light" style="top:253px;height:72px">
    <span class="step-tab">Step 3</span>
    <span class="opt" style="left:11px;top:20px"><i class="dot yellow"></i>Original</span>
    <span class="opt" style="left:97px;top:20px"><i class="dot yellow"></i>BBQ</span>
    <span class="opt" style="left:168px;top:20px"><i class="dot yellow"></i>Garlic Paper</span>
    <span class="opt" style="left:282px;top:20px"><i class="dot yellow"></i>Lemon</span>
    <span class="opt" style="left:372px;top:20px"><i class="dot yellow"></i>Dynamite</span>
    <span class="opt" style="left:128px;top:44px"><i class="dot yellow"></i>Buffalo</span>
    <span class="opt" style="left:207px;top:43px"><i class="dot yellow"></i>Nashville oh Hot Damn</span>
  </div>

  <div class="step-box light" style="top:346px;height:45px">
    <span class="step-tab">Step 4</span>
    <span class="opt" style="left:10px;top:17px"><i class="dot yellow"></i>Blue cheese</span>
    <span class="opt" style="left:107px;top:17px"><i class="dot yellow"></i>House ranch</span>
    <span class="opt" style="left:214px;top:17px"><i class="dot yellow"></i>Honey mustard</span>
    <span class="opt" style="left:329px;top:17px"><i class="dot yellow"></i>Roost special</span>
  </div>
</section>

<section>
  <div class="abs" style="left:534px;top:180px">
    <h2 class="sec-title">Sandwich Option 1</h2>
    <p class="sec-note">All meals servived with chips and dip</p>
  </div>
  <article class="item" style="top:227px"><h3>1. Classic Burger</h3><p>Fried Chicken Breast, Fresh Pickles &amp; Creamy Mayo In A Soft Brioche Bun</p><span class="price">6.99 £</span></article>
  <article class="item" style="top:285px"><h3>2. Roost Special</h3><p>Relish Sauce, Fried Chicken Breast,honey Mustard, Red Cabbage In A Soft Brioche Bun</p><span class="price">6.95 £</span></article>
  <article class="item" style="top:342px"><h3>3. Nashville Oh Hot Damn</h3><p style="margin-top:5px">Fried Nashville Chicken Breast, Fresh Pickles &amp; Roost Sause, Pot Of Grave&amp; Mash Potato</p><span class="price">7.99 £</span></article>
  <article class="item" style="top:402px"><h3>5. Double Cheesy Toasted</h3><p style="margin-top:5px">Tenders ,Cheese, Slaw, Pickles, Mayo</p><span class="price">5.99 £</span></article>
  <article class="item" style="top:451px;left:532px;width:278px"><h3>6. Dynamite Burger</h3><p style="margin-top:5px;width:210px">Sweet Mayo, Iceberg Lettuce, Fried Chicken Breast, Dynamite Sauce , Soft Deli Rolls</p><span class="price">6.50 £</span></article>
  <article class="item" style="top:511px;left:532px;width:278px"><h3>7. Mini Fillet Slider</h3><p style="margin-top:5px;width:225px">( Lemon Herbs , Demled Peri Peri , Mangolime) ( Mini Fillet , Lettus , Cheese , Select Your Flavoursin A Mini Bun)</p><span class="price">4.99 £</span></article>
</section>

<section>
  <div class="abs" style="left:859px;top:179px">
    <h2 class="sec-title">Sandwich Option 2</h2>
    <p class="sec-note">Sandwich &nbsp;All Meals Servied With Chips And Dip</p>
  </div>
  <div class="build" style="top:228px">
    <h4><b>Step 1</b>&nbsp; Select Your Base</h4><span class="price">2.50 £</span>
    <div class="choices" style="grid-template-columns:150px 140px"><span><i class="dot"></i>Brioche Bun</span><span><i class="dot"></i>Soft Deli Roll</span><span><i class="dot"></i>Double Chesney Toasted</span><span><i class="dot"></i>Waffle</span></div>
  </div>
  <div class="build" style="top:301px">
    <h4><b>Step 2</b>&nbsp; Select Your Chicken</h4><span class="price">3.50 £</span>
    <div class="choices" style="grid-template-columns:65px 140px;margin-top:9px"><span><i class="dot"></i>Tenders</span><span><i class="dot"></i>Chicken Breasrt</span></div>
  </div>
  <div class="build" style="top:357px">
    <h4><b>Step 3</b>&nbsp; Select Your Favourite Sause</h4><span class="price">2.50 £</span>
    <div class="choices" style="grid-template-columns:78px 71px 120px;margin-top:9px;row-gap:8px"><span><i class="dot"></i>Classics</span><span><i class="dot"></i>Buffalo</span><span><i class="dot"></i>Mangi Lime</span><span><i class="dot"></i>Daynmat</span><span><i class="dot"></i>Nashville</span><span><i class="dot"></i>Lemon Herbs</span><span><i class="dot"></i>Bbq</span><span style="grid-column:span 2"><i class="dot"></i>Demless Peri Peri</span></div>
  </div>
  <div class="build" style="top:447px">
    <h4><b>Step 4</b>&nbsp; Add Topping</h4><span class="price">0.00 £</span>
    <div class="choices" style="grid-template-columns:59px 65px 52px 70px;margin-top:7px"><span><i class="dot"></i>Cheese</span><span><i class="dot"></i>Cheese</span><span><i class="dot"></i>Slaw</span><span><i class="dot"></i>Pickles</span></div>
  </div>
  <div class="build" style="top:504px">
    <h4><b>Step 5</b>&nbsp; Select Your Sause</h4><span class="price">0.00 £</span>
    <div class="choices" style="grid-template-columns:120px 140px;margin-top:8px;row-gap:8px"><span><i class="dot"></i>Blue Cheese</span><span><i class="dot"></i>House Ranch</span><span><i class="dot"></i>Roost Special</span><span><i class="dot"></i>Honey Mustard</span><span><i class="dot"></i>Daynmaited</span></div>
  </div>
</section>

<section class="abs sides">
  <h2 class="sides-tab">Signature Side / Loaded Chips</h2>
  <i class="divider" style="left:302px"></i>
  <i class="divider" style="left:588px"></i>
  <i class="divider" style="left:872px"></i>

  <article class="side" style="left:18px;top:27px;width:260px"><h3>1. Chicken Pop Corn</h3><p>Chicken Pop Corn Topped With Meltd Cheddar Cheese , Dynamite Sasue , Sismes</p><span class="price">5.50 £</span></article>
  <article class="side" style="left:18px;top:85px;width:260px"><h3>2. Chilli Cheese Bites</h3><p>Chilli Cheese Bites , Select Your Dip</p><span class="price">5.50 £</span></article>
  <article class="side" style="left:18px;top:129px;width:242px"><h3>3. Mozerla Stick</h3><span class="price">£</span></article>

  <article class="side" style="left:322px;top:27px;width:245px"><h3>4. Halomi Stick</h3><span class="price">£</span></article>
  <article class="side" style="left:322px;top:58px;width:245px"><h3>5. Garlic Mushrooms Bites</h3><span class="price">£</span></article>
  <article class="side" style="left:322px;top:89px;width:245px"><h3>6. Onion Rings</h3><span class="price">£</span></article>
  <div class="extras"><span><i class="dot"></i>Mac &amp; cheese bites</span><span><i class="dot"></i>Roost special ( mash potato, grave sause )</span><span><i class="dot"></i>Honey mustard slaw</span></div>

  <article class="side" style="left:610px;top:27px;width:246px"><h3>Fry By</h3><p>Chips Loaded With Melted Cheese, Daynmite Sause, Jalapeño</p><span class="price">£</span></article>
  <article class="side" style="left:610px;top:83px;width:246px"><h3>Blazers Loaded</h3><p>Chips Load3d With Melted Cheese, Hot Sause, Blazers</p><span class="price">£</span></article>
  <article class="side" style="left:609px;top:138px;width:247px"><h3>Crunchoos</h3><p>Chips Tenders Loaded With Nelt3d Cheese, Ketchup, Crunchos</p><span class="price">£</span></article>

  <article class="side" style="left:895px;top:27px;width:246px"><h3>Oh Hot Damn</h3><p style="width:190px">Chips Nashville Tender , Melted Cheese , Sarcha Sause, Green Chilli Paper</p><span class="price">£</span></article>
  <article class="side" style="left:895px;top:83px;width:246px"><h3>Pop Corn</h3><p style="width:200px">Chips Chicken Pop Corn, Melted Cheese, Daynmaited Sause, Sesame</p><span class="price">£</span></article>
  <article class="side" style="left:895px;top:138px;width:246px"><h3>Pop Corn</h3><p style="width:200px">Chips , Tenders , Montero Jack Cheese, Crispy Fried Onion, Roost Dressing</p><span class="price">£</span></article>
</section>

</body>
</html>
```